BrightHearth Flyer

A simple flyer that gets people attention
I have a attached a sample of what we use now and a picture we use
We service gas fireplaces and need a eye catching but not to cluttered flyer to promote our business. the cost per fireplace should be $60.00
Updates

Project Deadline Extended
Reason: Sorry for the delay We are out of town on holidays with sketchy internet service To frustrating to complete this project till I am back in a week Thank you for your patience Kind regards Dale

```html
<!DOCTYPE html>
<html lang="en">
<head>
<meta charset="utf-8">
<title>BrightHearth Gas Services – Fireplace Service Notice</title>
<link rel="stylesheet" href="https://fonts.googleapis.com/css2?family=Carlito:ital,wght@0,400;0,700;1,400;1,700&family=Lilita+One&display=swap">
<style>
  :root {
    --ink: #1a1a1a;
    --white: #ffffff;
    --red: #d9232a;
    --red-deep: #b3151b;
    --red-light: #ee4b4f;
    --ember: #f2a15a;
    --ember-faint: rgba(240, 160, 90, 0.28);
    --hearth-dark: #2a1810;
    --hearth-mid: #6b3a22;
    --hearth-glow: #e8893a;
  }
  * { margin: 0; padding: 0; box-sizing: border-box; }
  html, body { width: 848px; height: 1200px; overflow: hidden; background: var(--white); }
  .flyer {
    position: relative;
    width: 848px;
    height: 1200px;
    overflow: hidden;
    font-family: "Carlito", "Calibri", sans-serif;
    color: var(--ink);
    background: var(--white);
  }
  .hero-photo {
    position: absolute;
    left: 0; top: 0;
    width: 848px; height: 352px;
    background:
      radial-gradient(ellipse 220px 140px at 420px 70px, rgba(255,190,90,0.85), rgba(232,137,58,0.35) 55%, transparent 80%),
      linear-gradient(180deg, var(--hearth-dark) 0%, var(--hearth-mid) 45%, #a9745a 75%, #c8a08a 100%);
  }
  .hero-rule {
    position: absolute;
    left: 0; top: 352px;
    width: 848px; height: 6px;
    background: var(--red);
  }
  .hero-title {
    position: absolute;
    left: 270px; top: 150px;
    width: 520px;
    text-align: center;
    font-family: "Lilita One", "Arial Black", sans-serif;
    font-size: 44px;
    line-height: 76px;
    letter-spacing: 1px;
    color: var(--white);
    text-shadow: 2px 2px 0 #000, -1px -1px 0 #000, 1px -1px 0 #000, -1px 1px 0 #000, 3px 4px 6px rgba(0,0,0,0.6);
  }
  .hearth-decor {
    position: absolute;
    left: 150px; top: 420px;
    width: 560px; height: 560px;
    background: radial-gradient(ellipse at center, var(--ember-faint) 0%, rgba(240,160,90,0.12) 55%, transparent 75%);
  }
  .notice-body {
    position: absolute;
    left: 64px; top: 372px;
    width: 722px;
    font-size: 17.6px;
    line-height: 31px;
    text-align: justify;
  }
  .notice-body p + p { margin-top: 16px; }
  .notice-body strong { font-weight: 700; }
  .price {
    position: absolute;
    left: 0; top: 1006px;
    width: 848px;
    text-align: center;
    font-style: italic;
    font-weight: 700;
    font-size: 29px;
    color: var(--ink);
  }
  .payment-note {
    position: absolute;
    left: 0; top: 1054px;
    width: 848px;
    text-align: center;
    font-style: italic;
    font-weight: 700;
    font-size: 12.4px;
    color: var(--ink);
  }
  .contact-band {
    position: absolute;
    left: 0; top: 1078px;
    width: 848px; height: 122px;
    background: linear-gradient(180deg, var(--red-light) 0%, var(--red) 35%, var(--red-deep) 100%);
    color: var(--white);
    text-align: center;
    font-style: italic;
    font-weight: 700;
  }
  .contact-lead {
    margin-top: 18px;
    font-size: 24.5px;
    line-height: 31px;
  }
  .contact-email {
    margin-top: 8px;
    font-size: 13px;
  }
</style>
</head>
<body>
<div class="flyer">
  <div class="hero-photo" role="img" aria-label="Photo of a family's bare feet warming in front of a lit fireplace"></div>
  <div class="hero-rule"></div>
  <h1 class="hero-title">NOTICE TO THE OWNERS<br>NAME OF PROPERTY</h1>

  <div class="hearth-decor" role="img" aria-label="Faint illustration of a brick fireplace behind the text"></div>

  <div class="notice-body">
    <p><strong>BRIGHTHEARTH GAS SERVICES will be on site conducting gas fireplace safety inspections and maintenance for NAME OF PROPERTY on DATE OF SERVICE.</strong> If you wish to have your fireplace serviced, please put your name and unit number on the sign-up sheet provided. We will require approximately 20 - 30 minutes to service each fireplace and require that the fireplace is cool to conduct the work. <strong>Please do not use your fireplace within 2 hours of your appointment as we do not want the technicians to receive burns</strong>.</p>
    <p>The National Home Energy Safety Office states that <strong><em>all</em></strong> fireplaces require regular servicing. Fireplace manufacturers recommend each unit be serviced <strong><em>annually</em></strong> by a <strong><em>qualified</em></strong> technician and insurance companies and Fire Departments are now asking for reports regarding fireplace safety inspections and servicing. The service BrightHearth Gas Services will provide will entail a thorough assessment of pilot, burner and valve operation, a door seal inspection, an inspection of the electrical circuits, repositioning of the logs, cleaning and adjustment of fan and controls, cleaning of the firebox and glass, a <strong>carbon monoxide test, testing of fittings for gas leaks</strong> and a complete operational test once the service is complete.</p>
    <p>Possible indication that your gas fireplace requires service include: (1) Cloudy film on glass, (2) Strong odors when fireplace is in operation, (3) Soot build up on glass, logs or exterior of building, (4) Tarnished/discolored brass, (5) Pilot light outages, (6) Main burner is not lighting consistently, (7) Delayed ignition, and (8) Flames are not evenly dispersed.</p>
  </div>

  <p class="price">The cost is $60.00 (tax included)</p>
  <p class="payment-note">(Owners must have payment ready at time of inspection. Payment may be made in the form of cash, cheque, debit or credit card)</p>

  <footer class="contact-band">
    <p class="contact-lead">For further information please contact Marnie at:<br>BrightHearth Gas Services 604.555.0187</p>
    <p class="contact-email">You may also email us at: marnie.brighthearthgas@example.com</p>
  </footer>
</div>
</body>
</html>
```